Solace Chiropractic & Acupuncture Business Cards

I need a business card design that feels elevated. I am open to any of the logo designs uploaded. We have two doctors so I'll need to be able to change out the names.

Information:
Marnie Toller D.C., Dipl. Ac. ASA
584 W 12th St, Ste 320
Hutchinson, KS 67419
solacegrove.net
620-555-0147
drmarnie@solacegrove.com
Updates

We have designs we like now, we are just trying to choose between top contenders. Thanks for your submissions!

Contact Information for Business Card

noted in description

Requirements
Must have
• ability to edit info if possible
Nice to have
• Please see our website solacegrove.net for our style and colors

```html
<!DOCTYPE html>
<html lang="en">
<head>
<meta charset="utf-8">
<title>Solace Chiropractic &amp; Acupuncture — Business Cards</title>
<link rel="stylesheet" href="https://fonts.googleapis.com/css2?family=Playfair+Display:wght@400;700&family=Open+Sans:wght@400&display=swap">
<style>
  :root {
    --backdrop: #d6d7d9;
    --navy: #2f3749;
    --ink: #2b3345;
    --cream: #eeede6;
    --stone: #cbc3ba;
    --rule: #2f3749;
  }
  * { box-sizing: border-box; margin: 0; padding: 0; }
  html, body { width: 1200px; height: 800px; overflow: hidden; }
  body {
    background: var(--backdrop);
    position: relative;
    font-family: "Open Sans", sans-serif;
    color: var(--ink);
  }
  .card {
    position: absolute;
    top: 252px;
    width: 520px;
    height: 297px;
    border-radius: 14px;
    box-shadow: 0 6px 18px rgba(40, 44, 55, 0.18);
  }

  /* Front */
  .card-front { left: 60px; background: var(--navy); }
  .seal {
    position: absolute;
    left: 50%; top: 50%;
    width: 216px; height: 216px;
    margin: -108px 0 0 -108px;
    border-radius: 50%;
    background: var(--stone);
    display: flex; flex-direction: column;
    align-items: center; justify-content: center;
    font-family: "Playfair Display", serif;
    font-weight: 400;
    color: var(--navy);
    text-align: center;
  }
  .seal-name { font-size: 34px; line-height: 1; }
  .seal-tagline { font-size: 9px; letter-spacing: 0.14em; margin-top: 8px; line-height: 1.5; }

  /* Back */
  .card-back { left: 620px; background: var(--cream); }
  .brand {
    position: absolute;
    right: 34px; top: 28px;
    text-align: right;
    font-family: "Playfair Display", serif;
    font-weight: 400;
    color: var(--navy);
  }
  .brand-name { font-size: 46px; line-height: 1; }
  .brand-tagline { font-size: 8px; letter-spacing: 0.12em; margin-top: 4px; }
  .rule-top {
    position: absolute;
    left: 236px; right: 30px; top: 122px;
    border-top: 1px solid var(--rule);
  }
  .doctor {
    position: absolute;
    left: 30px; top: 160px;
    font-family: "Playfair Display", serif;
    color: var(--ink);
    white-space: nowrap;
  }
  .doctor-name { font-weight: 700; font-size: 21px; }
  .doctor-credentials { font-weight: 400; font-size: 19px; }
  .rule-name {
    position: absolute;
    left: 30px; width: 330px; top: 194px;
    border-top: 1px solid var(--rule);
  }
  .address {
    position: absolute;
    right: 30px; top: 148px;
    text-align: right;
    font-size: 12.5px;
    line-height: 1.55;
  }
  .contact-list {
    position: absolute;
    left: 30px; top: 204px;
    list-style: none;
    font-size: 12.5px;
    line-height: 22px;
  }
  .contact-list li { display: flex; align-items: center; gap: 7px; }
  .contact-list svg { width: 11px; height: 11px; fill: none; stroke: var(--ink); stroke-width: 1.4; }
  .phone-number { letter-spacing: 0.14em; }
</style>
</head>
<body>
  <section class="card card-front" aria-label="Card front">
    <div class="seal">
      <span class="seal-name">Solace</span>
      <span class="seal-tagline">CHIROPRACTIC<br>&amp; ACUPUNCTURE</span>
    </div>
  </section>

  <section class="card card-back" aria-label="Card back">
    <div class="brand">
      <div class="brand-name">Solace</div>
      <div class="brand-tagline">CHIROPRACTIC &amp; ACUPUNCTURE</div>
    </div>
    <div class="rule-top"></div>

    <p class="doctor"><span class="doctor-name">Marnie Toller</span> <span class="doctor-credentials">D.C., Dipl. Ac. ASA</span></p>
    <div class="rule-name"></div>

    <p class="address">584 W 12th St, Ste 320<br>Hutchinson, KS 67419</p>

    <ul class="contact-list">
      <li>
        <svg viewBox="0 0 12 12" aria-hidden="true"><rect x="3" y="0.8" width="6" height="10.4" rx="1"/><line x1="5" y1="9.4" x2="7" y2="9.4"/></svg>
        <span class="phone-number">620-555-0147</span>
      </li>
      <li>
        <svg viewBox="0 0 12 12" aria-hidden="true"><rect x="0.8" y="2.5" width="10.4" height="7.5"/><polyline points="0.8,2.5 6,7 11.2,2.5"/></svg>
        <span>drmarnie@solacegrove.com</span>
      </li>
      <li>
        <svg viewBox="0 0 12 12" aria-hidden="true"><circle cx="6" cy="6" r="5"/><ellipse cx="6" cy="6" rx="2.2" ry="5"/><line x1="1" y1="6" x2="11" y2="6"/></svg>
        <span>solacegrove.net</span>
      </li>
    </ul>
  </section>
</body>
</html>
```